Create a Poster for a True Crime Tour

Velvet Hook True Crime Tour Poster Design

We need a square and a4 sized poster to promote a true crime tour.

The tour covers stories from 1920s-1930s australia in a period known as the velvet hook wars. The leader of the gang in those days was a female (hence the uploaded image).

Feel free to use this image or find one of your own choosing - I am interested in seeing your interpretation.

Key words that may help trigger ideas (I'm sure there are others I haven't thought of!!):-
scar
razor
torn paper
old film
1920s
border
the gange leader was a female
velvet hook true crime tour
australia
scratch marks

Target Market(s)

20-55 Age Group (70% female)

Industry/Entity Type

Tour

Requirements
Must have
• Include the following phrases:-
• Velvet Hook
• True Crime Tour

```html
<!DOCTYPE html>
<html lang="en">
<head>
<meta charset="utf-8">
<title>Velvet Hook True Crime Tour</title>
<link href="https://fonts.googleapis.com/css2?family=Abril+Fatface&family=Catamaran:wght@700;800;900&family=Open+Sans:ital,wght@1,300&display=swap" rel="stylesheet">
<style>
  :root {
    --ink: #141414;
    --paper: #ffffff;
    --blood: #7a1f24;
    --night: #050505;
    --hair: #1c1c1c;
    --skin-shadow: #6f6f6f;
    --skin-light: #d6d6d6;
    --skin-bright: #ececec;
    --muted: #333333;
  }
  * { margin: 0; padding: 0; box-sizing: border-box; }
  html, body { width: 800px; height: 1200px; overflow: hidden; background: var(--paper); }
  .poster { position: relative; width: 800px; height: 1200px; background: var(--paper); overflow: hidden; }

  .info-panel { position: absolute; left: 0; top: 0; width: 428px; height: 1200px; background: var(--paper); }

  .title {
    position: absolute; left: 0; top: 88px; width: 428px; text-align: center;
    font-family: "Abril Fatface", serif; font-size: 86px; line-height: 94px; letter-spacing: 1px;
    color: transparent;
    background: repeating-linear-gradient(to bottom, var(--ink) 0 2px, var(--paper) 2px 4px);
    -webkit-background-clip: text; background-clip: text;
    -webkit-text-stroke: 2px var(--ink);
  }
  .years {
    position: absolute; left: 0; top: 270px; width: 428px; text-align: center;
    font-family: "Catamaran", sans-serif; font-weight: 900; font-size: 32px; letter-spacing: -0.5px; color: var(--ink);
  }

  .tour-badge { position: absolute; left: 110px; top: 375px; width: 202px; height: 181px; }
  .tour-badge svg { position: absolute; left: 0; top: 0; }
  .tour-label {
    position: absolute; left: 22px; top: 18px; width: 160px; text-align: center;
    font-family: "Catamaran", sans-serif; font-weight: 900; color: var(--ink); line-height: 0.86; letter-spacing: -2px;
  }
  .tour-label span { display: block; }
  .tour-label .l1 { font-size: 62px; }
  .tour-label .l2 { font-size: 54px; margin-top: 0; }
  .tour-label .l3 { font-size: 58px; margin-top: 0; }

  .law-quote {
    position: absolute; left: 0; top: 606px; width: 400px; text-align: center;
    font-family: "Catamaran", sans-serif; font-weight: 800; color: var(--ink); line-height: 41px;
    letter-spacing: -0.3px;
  }
  .law-quote .sm { font-size: 25px; }
  .law-quote .lg { font-size: 38px; font-weight: 900; }
  .law-source {
    position: absolute; left: 120px; top: 779px; width: 282px; text-align: right;
    font-family: "Open Sans", sans-serif; font-style: italic; font-weight: 300; font-size: 23px; color: var(--muted);
    text-shadow: 1px 1px 2px rgba(0,0,0,0.2);
  }

  .tagline {
    position: absolute; left: 20px; top: 966px; width: 356px; text-align: right;
    font-family: "Catamaran", sans-serif; font-weight: 900; font-size: 39px; line-height: 48px; color: var(--ink);
    letter-spacing: -0.5px;
    text-shadow: 1px 2px 2px rgba(0,0,0,0.25);
  }
  .tagline .accent { color: var(--blood); font-size: 47px; }

  .portrait {
    position: absolute; left: 428px; top: 0; width: 372px; height: 1200px;
    background:
      linear-gradient(to bottom, var(--hair) 0%, rgba(28,28,28,0.85) 22%, rgba(28,28,28,0) 40%),
      linear-gradient(to right, var(--night) 0%, var(--night) 12%, var(--skin-shadow) 30%, var(--skin-light) 50%, var(--skin-bright) 100%);
  }

  .brand-mark {
    position: absolute; left: 604px; top: 1048px; width: 174px; height: 112px;
    border-radius: 50%; background: var(--night);
    display: flex; align-items: center; justify-content: center;
    font-family: "Catamaran", sans-serif; font-weight: 800; font-size: 20px; letter-spacing: 0.5px; color: var(--paper);
  }
</style>
</head>
<body>
<main class="poster">
  <section class="info-panel">
    <h1 class="title">VELVET<br>HOOKS</h1>
    <p class="years">1927-1931</p>

    <div class="tour-badge">
      <svg width="202" height="181" viewBox="0 0 202 181" aria-hidden="true">
        <polyline points="112,1 1,1 1,101" fill="none" stroke="#141414" stroke-width="2"/>
        <polyline points="201,119 201,180 73,180" fill="none" stroke="#141414" stroke-width="2"/>
      </svg>
      <h2 class="tour-label"><span class="l1">TRUE</span><span class="l2">CRIME</span><span class="l3">TOUR</span></h2>
    </div>

    <blockquote class="law-quote">
      <span class="sm">“A person shall </span><span class="lg">not</span><br>
      <span class="lg">purchase, carry,</span><br>
      <span class="sm">or have in his </span><span class="lg">possession</span><br>
      <span class="sm">any </span><span class="lg">pistol...”</span>
    </blockquote>
    <p class="law-source">Pistol Licensing Act of 1927</p>

    <p class="tagline">... they <span class="accent">killed</span> with<br><span class="accent">razors</span> instead.</p>
  </section>

  <div class="portrait" role="img" aria-label="Black and white portrait of a 1920s woman with finger-waved dark hair, a red eye and red lips, holding a bloodied straight razor at her throat, set against a black background"></div>

  <div class="brand-mark">Night Ledger</div>
</main>
</body>
</html>
```